8 behaviours infographic

We are a portfolio of approx. 200 resources in technology within a financial services enterprise (5000-6000 employees).
Our portfolio name is Harbour and Planner Asset Services.
Our leadership team has collectively defined a set of 8 behaviours that represent how we should behave and interact amongst ourselves.
We need an infographic that can bring these behaviours to life and be displayed around the workplace on large posters where teams work (the words for the behaviours should also be incorporated into the infographic).
We have also included our team's logo, which needs to be incorporated into the infographic.
The 8 behaviours are:
- Listen & show you care
- Support Each Other
- Be Accountable
- Communicate openly
- Collaborate and leverage the collective strength of the group
- Influence the agenda
- Proactive deliberate and team focussed
- Celebrate success & have fun
Look and feel
Each slider illustrates characteristics of the customer's brand and the style your logo design should communicate.

```html
<!DOCTYPE html>
<html lang="en">
<head>
<meta charset="utf-8">
<title>Harbour and Planner Asset Services – Our 8 Behaviours</title>
<link href="https://fonts.googleapis.com/css2?family=Comic+Neue:wght@400;700&family=Courier+Prime&family=Mr+Dafoe&display=swap" rel="stylesheet">
<style>
  :root {
    --hex-blue: #0277bd;
    --icon-white: #ffffff;
    --ink: #1b1f2a;
    --title-navy: #0c1526;
    --accent-blue: #0d7bc4;
    --bg-light: #ffffff;
    --bg-edge: #e9e9ea;
  }
  * { margin: 0; padding: 0; box-sizing: border-box; }
  html, body { width: 1200px; height: 1000px; overflow: hidden; }
  body {
    background: radial-gradient(ellipse at 45% 40%, var(--bg-light) 40%, var(--bg-edge) 100%);
    position: relative;
    font-family: "Comic Neue", sans-serif;
    color: var(--ink);
  }
  .honeycomb { position: absolute; left: 0; top: 0; width: 1200px; height: 1000px; }
  .hex { fill: var(--hex-blue); }
  .icon { fill: none; stroke: var(--icon-white); stroke-width: 3; stroke-linecap: round; stroke-linejoin: round; }
  .behaviour {
    position: absolute;
    font-size: 21px;
    line-height: 28px;
    text-align: center;
    white-space: nowrap;
    transform: translateX(-50%);
    letter-spacing: 0.3px;
  }
  .title {
    position: absolute;
    left: 0; width: 1200px;
    text-align: center;
  }
  .title-script {
    top: 700px;
    font-family: "Mr Dafoe", cursive;
    font-size: 140px;
    line-height: 160px;
    color: var(--title-navy);
  }
  .title-mono {
    top: 855px;
    font-family: "Courier Prime", monospace;
    font-size: 90px;
    line-height: 100px;
    color: var(--accent-blue);
  }
</style>
</head>
<body>
<svg class="honeycomb" viewBox="0 0 1200 1000" aria-hidden="true">
  <defs>
    <polygon id="hexagon" points="0,-96 83,-48 83,48 0,96 -83,48 -83,-48"/>
  </defs>
  <use href="#hexagon" class="hex" x="452" y="186"/>
  <use href="#hexagon" class="hex" x="624" y="186"/>
  <use href="#hexagon" class="hex" x="970" y="186"/>
  <use href="#hexagon" class="hex" x="194" y="337"/>
  <use href="#hexagon" class="hex" x="366" y="337"/>
  <use href="#hexagon" class="hex" x="710" y="337"/>
  <use href="#hexagon" class="hex" x="882" y="337"/>
  <use href="#hexagon" class="hex" x="452" y="488"/>
  <use href="#hexagon" class="hex" x="970" y="488"/>
  <use href="#hexagon" class="hex" x="366" y="638"/>
  <use href="#hexagon" class="hex" x="538" y="638"/>

  <!-- speech bubbles -->
  <g class="icon" transform="translate(452,186)">
    <path d="M-30,-38 h44 a14,14 0 0 1 14,14 v22 a14,14 0 0 1 -14,14 h-30 l-18,14 v-14 a14,14 0 0 1 -10,-14 v-22 a14,14 0 0 1 14,-14z"/>
    <circle cx="-20" cy="-13" r="3"/><circle cx="-8" cy="-13" r="3"/><circle cx="4" cy="-13" r="3"/>
    <path d="M30,-6 h2 a12,12 0 0 1 12,12 v14 a12,12 0 0 1 -8,12 v14 l-16,-14 h-22 a12,12 0 0 1 -12,-12 v-2"/>
  </g>
  <!-- ear -->
  <g class="icon" transform="translate(624,186)">
    <path d="M-30,30 c4,10 18,12 22,2 c4,-12 12,-16 18,-26 c10,-16 4,-44 -22,-44 c-20,0 -32,16 -30,34"/>
    <path d="M-26,-8 c0,-14 10,-22 20,-20 c12,2 14,16 6,24 c-6,6 -12,0 -8,8"/>
    <path d="M22,-14 c6,8 6,20 0,28"/><path d="M32,-22 c10,14 10,30 0,44"/><path d="M42,-30 c14,20 14,40 0,60"/>
  </g>
  <!-- network person -->
  <g class="icon" transform="translate(194,337)">
    <circle r="20"/><circle cy="-6" r="7"/><path d="M-12,12 c4,-10 20,-10 24,0"/>
    <line y1="-20" y2="-36"/><circle cy="-42" r="6"/>
    <line y1="20" y2="36"/><circle cy="42" r="6"/>
    <line x1="-20" x2="-36"/><circle cx="-42" r="6"/>
    <line x1="20" x2="36"/><circle cx="42" r="6"/>
    <line x1="-14" y1="-14" x2="-26" y2="-26"/><circle cx="-30" cy="-30" r="5"/>
    <line x1="14" y1="-14" x2="26" y2="-26"/><circle cx="30" cy="-30" r="5"/>
    <line x1="-14" y1="14" x2="-26" y2="26"/><circle cx="-30" cy="30" r="5"/>
    <line x1="14" y1="14" x2="26" y2="26"/><circle cx="30" cy="30" r="5"/>
  </g>
  <!-- globe in hand -->
  <g class="icon" transform="translate(710,337)">
    <circle cx="8" cy="-18" r="26"/>
    <path d="M-6,-36 c6,6 2,12 8,14 c6,2 4,10 -2,12"/><path d="M22,-34 c-6,6 4,10 10,8"/><path d="M14,-2 c2,-6 10,-8 12,-2"/>
    <path d="M-50,22 h14 v24 h-14z"/>
    <path d="M-36,26 h18 c8,0 10,8 18,8 h14"/><path d="M-36,42 h30 c14,0 30,-10 42,-22 c4,-4 -2,-10 -8,-6 l-20,12"/>
  </g>
  <!-- calendar magnet -->
  <g class="icon" transform="translate(882,337)">
    <rect x="-40" y="-36" width="80" height="72" rx="8"/>
    <line x1="-40" y1="-18" x2="40" y2="-18"/>
    <line x1="-22" y1="-44" x2="-22" y2="-28"/><line x1="22" y1="-44" x2="22" y2="-28"/>
    <path d="M-8,-4 l-10,10 a12,12 0 0 0 17,17 l10,-10 l-7,-7 l-10,10 a2,2 0 0 1 -3,-3 l10,-10z"/>
    <line x1="-3" y1="1" x2="4" y2="8"/>
  </g>
  <!-- celebration glasses -->
  <g class="icon" transform="translate(452,488)">
    <path d="M-34,-10 l22,6 l-6,22 c-2,8 -14,10 -20,4 c-6,-6 -4,-22 4,-32z"/>
    <line x1="-20" y1="22" x2="-28" y2="44"/><line x1="-38" y1="40" x2="-18" y2="48"/>
    <path d="M34,-10 l-22,6 l6,22 c2,8 14,10 20,4 c6,-6 4,-22 -4,-32z"/>
    <line x1="20" y1="22" x2="28" y2="44"/><line x1="38" y1="40" x2="18" y2="48"/>
    <path d="M-22,-48 l3,7 7,1 -5,5 1,7 -6,-4 -6,4 1,-7 -5,-5 7,-1z"/>
    <path d="M18,-48 l3,7 7,1 -5,5 1,7 -6,-4 -6,4 1,-7 -5,-5 7,-1z"/>
    <line x1="0" y1="-50" x2="0" y2="-40"/>
  </g>
  <!-- people group -->
  <g class="icon" transform="translate(970,488)">
    <circle cy="-18" r="13"/><path d="M-22,22 v-6 a22,22 0 0 1 44,0 v6"/>
    <circle cx="-40" cy="-8" r="10"/><path d="M-58,22 v-2 a18,18 0 0 1 28,-14"/>
    <circle cx="40" cy="-8" r="10"/><path d="M58,22 v-2 a18,18 0 0 0 -28,-14"/>
    <line x1="-58" y1="22" x2="58" y2="22"/>
  </g>
  <!-- handshake -->
  <g class="icon" transform="translate(366,638)">
    <path d="M-50,-18 l14,-8 l14,28 l-12,8z"/><path d="M50,-18 l-14,-8 l-14,28 l12,8z"/>
    <path d="M-26,-10 c10,-6 18,-8 28,-4 l12,-4"/>
    <path d="M24,-12 l-22,2 c-8,2 -10,10 -2,12 l12,-4 l24,20"/>
    <path d="M-28,8 l8,8 m0,0 c4,4 10,0 6,-4 m0,0 l8,8 c4,4 10,0 6,-4 l6,6 c4,4 10,0 6,-4 l4,4 c4,4 10,-2 6,-6"/>
  </g>
  <!-- headset -->
  <g class="icon" transform="translate(538,638)">
    <path d="M-34,4 v-10 a34,34 0 0 1 68,0 v10"/>
    <rect x="-44" y="-2" width="14" height="30" rx="6"/><rect x="30" y="-2" width="14" height="30" rx="6"/>
    <path d="M-37,28 c0,14 10,22 24,22"/><rect x="-14" y="45" width="18" height="9" rx="4"/>
  </g>
</svg>

<div class="behaviour" style="left:277px;top:151px;">Communicate<br>openly</div>
<div class="behaviour" style="left:796px;top:151px;">Listen &amp; show<br>you care</div>
<div class="behaviour" style="left:1060px;top:309px;">Influence the<br>agenda</div>
<div class="behaviour" style="left:195px;top:436px;">Be Accountable</div>
<div class="behaviour" style="left:643px;top:458px;">Celebrate success<br>&amp; have fun</div>
<div class="behaviour" style="left:148px;top:594px;">Collaborate and<br>leverage the collective<br>strength of the group</div>
<div class="behaviour" style="left:702px;top:603px;">Support Each<br>Other</div>
<div class="behaviour" style="left:969px;top:588px;">Proactive<br>deliberate and<br>team focussed</div>

<h1 class="title title-script">Harbour and Planner</h1>
<p class="title title-mono">Asset Services</p>
</body>
</html>
```